Wine Label for New exciting wine company

We require a label thats quirky and stands out in the crowded shelves of liquor stores. We are happy to use such colours as burnt orange, reds etc, or we are opened to any new brave designs with designers choice of colours. Label not to be to busy, but must have a presence. Label size to be approx 9cm Width and 10cm Long.
By the way the name of the wine ladel is Tallowbrook Wines. The word Wines does not need to show on the label

Thanks
Ned Farrow

Hi Everyone, we had a label we started a few years back called Pinecrest Wines which was a very successful wine and is still being sold today. It was fun and funky and stood out on the shelf, and thats the sort of label we wanted designed. It can be along different lines but the concept is what we are looking at.
Please go to their site www.pinecrestwines-example.com.au and have a look at the label.
Saying that a couple of the sesigns that have come through have merit and will still be considered.
Thanks fot all your designs so far
Ned Farrow

```html
<!DOCTYPE html>
<html lang="en">
<head>
<meta charset="utf-8">
<title>Tallowbrook – Label Options</title>
<link rel="stylesheet" href="https://fonts.googleapis.com/css2?family=Poiret+One&family=Tenor+Sans&display=swap">
<style>
  :root {
    --backdrop: #1e1e20;
    --label-dark: #2b2c31;
    --cream: #fbf3bf;
    --gold: #f2b70f;
    --white: #f4f1e6;
    --orange: #ff6a00;
    --red: #c22a1e;
    --slate: #4a5060;
    --sun-yellow: #f6c94a;
    --amber: #e77d1e;
  }
  * { box-sizing: border-box; margin: 0; padding: 0; }
  html, body {
    width: 1200px; height: 848px; overflow: hidden;
    background: var(--backdrop);
  }
  .stage { position: relative; width: 1200px; height: 848px; }
  .label {
    position: absolute; top: 222px; height: 404px;
    background: var(--label-dark);
    overflow: hidden; text-align: center;
  }
  .label--triangles { left: 176px; width: 363px; }
  .label--zigzag { left: 698px; width: 322px; }
  .label__art { position: absolute; left: 0; top: 0; width: 100%; }
  .label--triangles .label__art {
    height: 188px;
    background: linear-gradient(180deg, var(--orange) 0%, var(--orange) 40%, var(--red) 72%, var(--slate) 100%);
  }
  .label--zigzag .label__art {
    height: 238px;
    background: linear-gradient(180deg, var(--sun-yellow) 0%, var(--sun-yellow) 22%, var(--orange) 45%, var(--amber) 62%, var(--slate) 85%, var(--label-dark) 100%);
  }
  .label__name {
    position: absolute; left: 0; width: 100%;
    font-family: "Poiret One", sans-serif;
    color: var(--cream);
    line-height: 1;
  }
  .label--triangles .label__name { top: 222px; font-size: 46px; letter-spacing: 1px; }
  .label--zigzag .label__name { top: 258px; font-size: 42px; letter-spacing: 0; }
  .label__region, .label__vintage, .label__variety {
    position: absolute; left: 0; width: 100%;
    font-family: "Tenor Sans", sans-serif;
    text-transform: uppercase; line-height: 1;
  }
  .label--triangles .label__region { top: 284px; font-size: 15px; letter-spacing: 2.5px; color: var(--gold); }
  .label--triangles .label__vintage { top: 340px; font-size: 15px; letter-spacing: 2px; color: var(--gold); }
  .label--triangles .label__variety { top: 362px; font-size: 14px; letter-spacing: 1.5px; color: var(--gold); }
  .label--zigzag .label__region { top: 310px; font-size: 12px; letter-spacing: 3px; color: var(--white); }
  .label--zigzag .label__vintage { top: 365px; font-size: 10px; letter-spacing: 3px; color: var(--white); }
  .label--zigzag .label__variety { top: 378px; font-size: 9px; letter-spacing: 3px; color: var(--white); }
</style>
</head>
<body>
<main class="stage">
  <section class="label label--triangles">
    <div class="label__art" role="img" aria-label="Geometric sunset over layered triangular mountain peaks in orange, red and slate"></div>
    <h1 class="label__name">TALLOWBROOK</h1>
    <p class="label__region">- Margaret River -</p>
    <p class="label__vintage">2007</p>
    <p class="label__variety">Cabernet Merlot</p>
  </section>

  <section class="label label--zigzag">
    <div class="label__art" role="img" aria-label="Sun over stacked zigzag mountain ridges in yellow, orange and slate"></div>
    <h2 class="label__name">TALLOWBROOK</h2>
    <p class="label__region">-Margaret River-</p>
    <p class="label__vintage">2007</p>
    <p class="label__variety">Cabernet Merlot</p>
  </section>
</main>
</body>
</html>
```